Brochure & Flyer Design

Coral Skipper Elmgrove - Fish & Chips is a popular fish and chip store located on Sydney’s beautiful northern beaches. It sits just across from the sandy shores of Newport Beach.
Please see attached:
1. Details on the brochure I would like designed for Coral Skipper Elmgrove
2. Current menu that is in store that will need to be included
3. Logo
I would like a modern, fresh design to complement the logo focusing on the food.
Here is the link to download the images that should be included in the brochure https://www.filedrift.net/fetch/PxKmTzQaVbRnLwYcJdHsKe
To complement the brochure I would like an A1 flyer template that can be used to promote specials at the store.

```html
<!DOCTYPE html>
<html lang="en">
<head>
<meta charset="utf-8">
<title>Coral Skipper Elmgrove - Fish &amp; Chips — Menu Brochure</title>
<link rel="stylesheet" href="https://fonts.googleapis.com/css2?family=Fredoka:wght@500;600&family=Baloo+2:wght@700;800&family=Quicksand:wght@500;600&display=swap">
<style>
  :root {
    --orange: #e8641c;
    --navy: #1f2f6e;
    --paper: #ffffff;
    --ink: #2a2f45;
    --divider-grey: #c9cbd0;
    --backdrop: #2c3038;
    --photo-a: #e9b04a;
    --photo-b: #b86c1f;
    --amount-grey: #8a8d96;
  }
  * { box-sizing: border-box; margin: 0; padding: 0; }
  html, body { width: 1200px; height: 870px; overflow: hidden; }
  body { background: var(--backdrop); font-family: "Quicksand", sans-serif; color: var(--ink); }

  .spread { position: absolute; left: 15px; top: 20px; display: flex; gap: 15px; }
  .panel {
    width: 380px; height: 830px; background: var(--paper);
    padding: 22px 22px 18px; display: flex; flex-direction: column;
  }

  .divider { display: block; border: 0; height: 4px; width: 100%; background: var(--orange); border-radius: 2px; flex-shrink: 0; }
  .divider--grey { background: var(--divider-grey); height: 4px; margin: 0; }

  .section-title {
    font-family: "Fredoka", sans-serif; font-weight: 600; color: var(--orange);
    font-size: 34px; line-height: 1.05; margin: 8px 0 6px;
  }
  .item-name {
    font-family: "Baloo 2", sans-serif; font-weight: 800; color: var(--navy);
    font-size: 23px; line-height: 1;
  }
  .item-desc { font-size: 13px; line-height: 1.3; color: var(--ink); }

  .row { display: flex; justify-content: space-between; align-items: flex-start; gap: 8px; }
  .entry { margin-bottom: 10px; }

  .price {
    display: inline-block; background: var(--navy); color: #fff;
    font-family: "Baloo 2", sans-serif; font-weight: 700; font-size: 14px;
    line-height: 1; padding: 4px 7px 3px; border-radius: 4px; white-space: nowrap;
  }
  .price .cur { font-size: 10px; margin-right: 3px; }
  .price--extra { background: var(--orange); }

  .photo {
    border-radius: 4px;
    background: radial-gradient(circle at 45% 40%, var(--photo-a), var(--photo-b) 75%);
  }
  .photo--burger { background: radial-gradient(circle at 50% 45%, #d99a4a, #9b5a22 70%); border-radius: 50% 50% 40% 40%; }

  /* panel 1 */
  .fish-list { font-size: 13px; line-height: 1.4; margin-top: 4px; }
  .special-foot { display: flex; justify-content: flex-end; margin: -4px 0 12px; }
  .salad { margin-bottom: 8px; }
  .salads-block { margin-bottom: 6px; }
  .pack-feature { display: flex; justify-content: space-between; margin-top: 4px; }
  .pack-feature .photo { width: 120px; height: 100px; }
  .pack-feature .price { align-self: flex-end; }

  /* panel 2 */
  .pack-row { position: relative; display: flex; justify-content: space-between; height: 146px; padding-top: 10px; }
  .pack-row .text { width: 170px; }
  .pack-row .item-name { font-size: 26px; }
  .pack-row .photo { width: 140px; height: 100px; }
  .pack-row .tags { position: absolute; right: 0; bottom: 10px; display: flex; gap: 6px; }

  /* panel 3 */
  .burger { display: flex; justify-content: space-between; height: 118px; }
  .burger .text { width: 190px; }
  .burger .item-name { font-size: 27px; }
  .burger .side { display: flex; flex-direction: column; align-items: flex-end; gap: 4px; }
  .burger .photo { width: 120px; height: 82px; }
  .combo {
    background: var(--navy); color: #fff; margin: 8px -22px 10px; padding: 12px 22px;
  }
  .combo .item-name { color: #fff; font-size: 28px; }
  .combo .price { background: #fff; color: var(--navy); }
  .combo .item-desc { color: #fff; }
  .builder { display: flex; gap: 12px; font-size: 14px; line-height: 1.45; }
  .builder ul { list-style: none; flex: 1; }
  .builder li { display: flex; justify-content: space-between; }
  .builder .amt { color: var(--amount-grey); }
  .builder .column-rule { width: 3px; background: var(--orange); }
</style>
</head>
<body>
<main class="spread">

  <section class="panel panel--meals">
    <hr class="divider">
    <h2 class="section-title">Family Meals</h2>
    <div class="entry">
      <div class="row"><h3 class="item-name">Fishermans Basket</h3><span class="price"><span class="cur">$</span>39.90</span></div>
      <p class="item-desc">2 Fillets of Fish, 6 Calamari Rings, 4 Prawns, 4 Sea Scallops, Large Chips, Lemon &amp; Sauce</p>
    </div>
    <div class="entry">
      <div class="row"><h3 class="item-name">Dinner Pack</h3><span class="price"><span class="cur">$</span>42.90</span></div>
      <p class="item-desc">4 Fillets of Fish, 12 Calamari Rings, Large Chips, Lemon &amp; Sauce</p>
    </div>

    <hr class="divider">
    <h2 class="section-title">Daily Fish Special</h2>
    <div class="entry">
      <div class="row"><h3 class="item-name">Grilled or Fried</h3><span class="price"><span class="cur">$</span>16.90</span></div>
      <p class="fish-list">Salmon<br>Barramundi<br>Snapper</p>
    </div>
    <div class="special-foot"><span class="price price--extra">+ CHIPS <span class="cur">$</span>3.00</span></div>

    <hr class="divider">
    <h2 class="section-title">Salads</h2>
    <div class="salads-block">
      <div class="row salad"><h3 class="item-name">Coleslaw Salad</h3><span class="price"><span class="cur">$</span>6.90</span></div>
      <div class="row salad"><h3 class="item-name">Garden Salad</h3><span class="price"><span class="cur">$</span>6.90</span></div>
    </div>

    <hr class="divider">
    <h2 class="section-title">Packs</h2>
    <div class="pack-feature">
      <div>
        <h3 class="item-name">Fish Cocktail<br>Pack</h3>
        <p class="item-desc">6 Fish Cocktails<br>and Chips</p>
      </div>
      <div class="photo" role="img" aria-label="Photo of fish cocktails with lemon in a takeaway box"></div>
      <span class="price"><span class="cur">$</span>13.90</span>
    </div>
  </section>

  <section class="panel panel--packs">
    <article class="pack-row">
      <div class="text"><h3 class="item-name">Junior<br>Pack</h3><p class="item-desc">2 Fish Cocktails, 2 Calamari Rings, 1 Seafood Stick and Chips</p></div>
      <div class="photo" role="img" aria-label="Photo of junior pack with fish cocktails, calamari and chips"></div>
      <div class="tags"><span class="price"><span class="cur">$</span>9.90</span></div>
    </article>
    <hr class="divider divider--grey">
    <article class="pack-row">
      <div class="text"><h3 class="item-name">Calamari<br>Pack</h3><p class="item-desc">8 Calamari Rings<br>and Chips</p></div>
      <div class="photo" role="img" aria-label="Photo of calamari rings and chips in a takeaway box"></div>
      <div class="tags"><span class="price"><span class="cur">$</span>11.90</span></div>
    </article>
    <hr class="divider divider--grey">
    <article class="pack-row">
      <div class="text"><h3 class="item-name">Fish and<br>Chips</h3><p class="item-desc">1 Fillet of fish<br>and Chips</p></div>
      <div class="photo" role="img" aria-label="Photo of battered fish fillet and chips in a takeaway box"></div>
      <div class="tags"><span class="price price--extra">GRILLED + <span class="cur">$</span>2.00</span><span class="price"><span class="cur">$</span>11.90</span></div>
    </article>
    <hr class="divider divider--grey">
    <article class="pack-row">
      <div class="text"><h3 class="item-name">Pawn<br>Pack</h3><p class="item-desc">6 Prawns<br>and Chips</p></div>
      <div class="photo" role="img" aria-label="Photo of prawns and chips in a takeaway box"></div>
      <div class="tags"><span class="price"><span class="cur">$</span>14.50</span></div>
    </article>
    <hr class="divider divider--grey">
    <article class="pack-row">
      <div class="text"><h3 class="item-name">Sea Scallop<br>Pack</h3><p class="item-desc">Sea Scallops<br>and Chips</p></div>
      <div class="photo" role="img" aria-label="Photo of sea scallops and chips in a takeaway box"></div>
      <div class="tags"><span class="price"><span class="cur">$</span>14.50</span></div>
    </article>
  </section>

  <section class="panel panel--burgers">
    <h2 class="section-title">Burgers</h2>
    <article class="burger">
      <div class="text"><h3 class="item-name">Outrigger<br>Burger</h3><p class="item-desc">4 Calamari Rings, Garden Lettuce, Tartare Sauce</p></div>
      <div class="side"><div class="photo photo--burger" role="img" aria-label="Photo of calamari burger"></div><span class="price"><span class="cur">$</span>7.90</span></div>
    </article>
    <article class="burger">
      <div class="text"><h3 class="item-name">Odessey<br>Burger</h3><p class="item-desc">Fish Fillet, Coleslaw Salad, Seafood Sauce</p></div>
      <div class="side"><div class="photo photo--burger" role="img" aria-label="Photo of fish fillet burger with coleslaw"></div><span class="price"><span class="cur">$</span>7.90</span></div>
    </article>
    <article class="burger">
      <div class="text"><h3 class="item-name">Olympiad<br>Burger</h3><p class="item-desc">Fish Fillet, Garden Lettuce, Fresh Tomato, Tartare Sauce</p></div>
      <div class="side"><div class="photo photo--burger" role="img" aria-label="Photo of fish burger with lettuce and tomato"></div><span class="price"><span class="cur">$</span>7.90</span><span class="price price--extra">GRILLED + <span class="cur">$</span>2.00</span></div>
    </article>

    <div class="combo">
      <div class="row"><h3 class="item-name">Burger combo</h3><span class="price"><span class="cur">$</span>19.90</span></div>
      <p class="item-desc">2 Burger with Chips and 600ml Water</p>
    </div>

    <h2 class="section-title">Create a Pack</h2>
    <div class="builder">
      <ul>
        <li>Fillets of Fish <span class="amt">$ 8.90</span></li>
        <li>Fish Cocktail <span class="amt">$ 2.40</span></li>
        <li>Calamari Rings <span class="amt">$ 1.20</span></li>
        <li>Prawn Cutlet <span class="amt">$ 2.40</span></li>
        <li>Sea Scallops <span class="amt">$ 1.00</span></li>
        <li>Ocean Mussel <span class="amt">$ 1.00</span></li>
        <li>Seafood Stick <span class="amt">$ 1.80</span></li>
      </ul>
      <div class="column-rule"></div>
      <ul>
        <li>Small Chips <span class="amt">$ 4.50</span></li>
        <li>Large Chips <span class="amt">$ 7.00</span></li>
        <li>Potato Scallop <span class="amt">$ 1.00</span></li>
        <li>Banana Fritter <span class="amt">$ 3.00</span></li>
        <li>Pineapple Fritter <span class="amt">$ 3.00</span></li>
        <li>Vegie Spring Roll <span class="amt">$ 2.50</span></li>
        <li>Extra Sauce <span class="amt">$ 0.50</span></li>
      </ul>
    </div>
  </section>

</main>
</body>
</html>
```